Marketing / Informational Site for Marriage and Family Therapists Cooperative

We need a web design for a new Marriage and Family Therapist Cooperative, called Meadowgate Counselors. This is a market and information site for potential clients and referrals to learn more about the team and get contact information.

We are looking for profession, clean, and modern design, that cater towards families and mom's concerned about their families mental health and child development.

This should include a home page, an general about page, 3 bio pages (1 for each therapist listed below), and a general contact us page.

Our Domain Name

Meadowgatecounselors.example

Company Name

Meadowgate Counselors

Group Moto/Philosophy

“Our sorrows and wounds are healed only when we touch them with compassion.” - Orvelan

Our Logo

See Heron Final (attached)

Home Page (Introduction)

Feeling stressed and overwhelmed?
Encountering barriers towards your goals?
Having difficulty accomplishing the simplest task?
Have the need to talk but unsure who to turn to?

Therapy can assist you in overcoming all of these challenges. Assist you in uncovering the difficulties and barriers that are keeping you from achieving your life’s ambitions, help discover ways to overcome them, and cope with the impact your behaviour has on your occupation, personal life and social life.

Welcome to our practice, with over 20 years of combined experience in the clinical field you are sure to find the right fit for your needs. Each clinician has experience working with groups, adults, teens, children, families, and couples. We specialize in fostering healthy relationships between individuals, managing depression and anxiety, overcoming trauma, and developing occupational success. Feel free to explore information about each clinician and make an appointment with one of us today.

About Us (bio pics attached)

Marisel Dunkworth

My name is Dr. MariSel Dunkworth and I am a Licensed Marriage Family Therapist with a practice in Riverside, CA. I have devoted my life’s work into developing my skills in this profession. I have over 15 years of experience working in the clinical and the social service settings. These years have afforded me the opportunity to work with groups, families, adults, teens and children with varying symptoms. I have helped clients that have trauma, abuse histories, and many within the legal or social service systems. I enjoy working individuals from all walks of life achieve self sufficiency, social success and occupational success. In my years of training I have come to develop a culturally sensitive practice that centers around the needs of the client.

I have held many positions in my clinical career beginning as clinician moving upwards toward supervisor and program coordinator. I have also over 5 years of experience as an adjunct faculty member in the University setting teaching student to become Marriage and Family Therapists. As a clinician I focused on enriching my clinical skills by developing outcome driven practices to achieve client’s desired goals. As a clinical supervisor, I guided clinicians along their own paths towards clinical licensure. As a program coordinator, I helped develop a clinical assessment and triage program from ground up to assist client in accessing services in the South Los Angeles Area. The program would assist over 100 plus clients on a monthly basis get connected to clinical services and linked to any additional resources as needed by the individual. I have graduated with my, Bachelor’s degree at the Halvern College, Riverside. I received my Masters degree in Clinical Psychology at Mount St. Mary’s University, and my Doctorate degree in Clinical Psychology at Tamsworth Institute.

To schedule an appointment with Dr. MariSel Dunkworth, Meadowgate Counselors:

email: marisel582@postbox.example
Phone: (951)555-0182

Jeb Kowal

My name is Rosalindra (Jeb) Kowal, I received my Masters Degree of Counseling in Marriage and Family Therapy from Corvell Bay State College in June 2000. I have acquired over 15 years of experience helping Individuals, Couples, and Families cope with issues of Anxiety, Depression, Grief and Bereavement, and HIV/AIDS.

I am a Family Systems Therapist and I truly believe the dynamics in our family of origin greatly shape our current belief systems and behaviors. However, I often utilize a variety of approaches to help my clients achieve their goals depending on their individual needs.

My greatest strength as a Marriage and Family Therapist is helping my clients explore ways to make the changes in their lives that will allow them to live their life to their fullest potential. I help my clients achieve their personal life goals with a warm, safe, non-judgmental , and supportive environment. In doing so, my clients are encouraged to explore the issues that may be preventing them from living the life they desire. Thus, empowering them to take control of their personal journey to living a productive and meaningful life.

If you feel that you are ready to commit to bringing about positive changes in your life and would like support in exploring this path, I’m here to work with you in your journey to personal growth and development.

To schedule an appointment with Rosalindra Kowal, Meadowgate Counselors:

e-mail: rkjeb7@mailnest.example
Phone: (951)555-0147

Dena Holcroft

Dena Holcroft graduated with a Masters in Marriage and Family Therapy from Pellridge Crestwood College. She currently holds a license in Marriage and Family Therapy in the State of California. She is also formally trained in Clinical Art Therapy. Dena's expertise lies in providing treatment to individuals experiencing work-related injuries, severe physical and emotional pain, trauma, grief and loss, anxiety and depression. In her early career, she provided valuable service at the largest free clinic in the nation serving marginalized families and children. For the past ten years, Dena has worked with HIV/AIDS population.
Dena comes from a multicultural background and she has utilized this experience and knowledge in serving a variety of populations. At an organizational level, Dena has worked extensively with challenging issues such as the chemical dependency and homelessness. In her private practice, Dena is proficient in working within individuals experiencing relationship concerns, marital and family conflict, depression/anxiety, self-esteem concerns, adjustment disorders, and pain management. She has treated clients from diverse cultural, linguistic backgrounds and sexual orientations.
Dena is trained in Family Systems Theory and incorporates other strategies appropriate for each presenting issue. She specializes in Clinical Art Therapy and has successfully utilized an integrated approach including guided imagery and relaxation skills training for many years.

To schedule an appointment with Dena Holcroft, Meadowgate Counselors

e-mail: greypinestudio@inkmail.example
Phone: (951) 555-0169

Target Market(s)

Families with child development, marriage issues, or other mental health needs

Industry/Entity Type

Marketing

Number of Pages Required

5+ page

Requirements
Must have
• 1 home page, 1 about page, 1 contact page. About page could either be standalone page with 3 different bio pages for each therapist or an all in one about page that includes bios for all 3 therapists.

```html
<!DOCTYPE html>
<html lang="en">
<head>
<meta charset="utf-8">
<title>Meadowgate Counselors</title>
<link href="https://fonts.googleapis.com/css2?family=Lato:ital,wght@0,300;0,400;0,700;1,300;1,400&family=Raleway:ital,wght@0,300;0,400;1,400&display=swap" rel="stylesheet">
<style>
:root{
  --green:#a8c24e;
  --green-dark:#8fab38;
  --green-soft:#d3e3a2;
  --ink:#2f342e;
  --text:#5b5f57;
  --white:#ffffff;
  --night:#221c19;
}
*{box-sizing:border-box;margin:0;padding:0}
html,body{width:1200px;height:2340px;overflow:hidden}
body{font-family:"Lato",sans-serif;color:var(--text);background:var(--white);position:relative}

.hero{position:absolute;left:0;top:0;width:1200px;height:652px;
  background:
    radial-gradient(ellipse 16% 26% at 25% 58%, rgba(128,170,198,.85) 0%, rgba(128,170,198,0) 100%),
    radial-gradient(ellipse 20% 34% at 48% 52%, rgba(150,158,170,.85) 0%, rgba(150,158,170,0) 100%),
    radial-gradient(ellipse 18% 30% at 70% 56%, rgba(226,176,160,.8) 0%, rgba(226,176,160,0) 100%),
    radial-gradient(ellipse 34% 22% at 50% 28%, rgba(196,150,124,.55) 0%, rgba(196,150,124,0) 100%),
    linear-gradient(180deg,#ecebe8 0%,#e2e0dc 55%,#f6f6f5 78%,#dcdad6 100%)}
.site-header{position:absolute;left:0;top:0;width:1200px;height:130px;display:flex;justify-content:space-between;align-items:flex-start;padding:30px 56px 0 64px}
.brand{display:flex;flex-direction:column;align-items:center;gap:8px;margin-top:6px}
.brand-dot{width:54px;height:54px;border-radius:50%;background:var(--green)}
.brand-name{font-size:20px;font-weight:400;color:var(--green-dark);letter-spacing:1px}
.main-nav{display:flex;gap:16px;margin-top:20px}
.main-nav a{font-size:20px;color:#222;text-decoration:none;padding:8px 18px;border-radius:6px}
.main-nav a.active{background:var(--green);color:var(--white);box-shadow:0 2px 4px rgba(0,0,0,.2)}

.quote-band{position:absolute;left:0;top:652px;width:1200px;height:148px;background:var(--green);display:flex;align-items:center;justify-content:center;text-align:center}
.quote-band p{font-family:"Raleway",sans-serif;font-style:italic;font-weight:400;color:var(--white);font-size:31px;line-height:44px;letter-spacing:.5px}

.welcome{position:absolute;left:0;top:800px;width:1200px;height:420px;text-align:center}
.welcome h1{font-family:"Raleway",sans-serif;font-weight:300;color:var(--green);font-size:54px;margin-top:34px}
.questions{margin-top:16px;font-size:21px;font-weight:700;color:#3b3f3a;line-height:32px}
.intro{width:940px;margin:18px auto 0;font-size:15px;line-height:22px;color:#555}
.btn{display:inline-block;background:var(--green);color:var(--white);font-size:19px;padding:9px 26px;border-radius:8px;box-shadow:0 3px 5px rgba(0,0,0,.28);text-decoration:none}
.welcome .btn{margin-top:22px}

.about{position:absolute;left:0;top:1220px;width:1200px;height:600px;background:var(--green-soft)}
.about h2{font-family:"Raleway",sans-serif;font-weight:400;font-size:62px;color:var(--ink);text-align:center;margin-top:20px}
.team{display:flex;justify-content:space-between;width:1100px;margin:18px auto 0}
.member{width:330px;text-align:center}
.portrait{width:250px;height:250px;margin:0 auto;border-radius:50%;border:9px solid var(--green);position:relative;overflow:hidden}
.portrait .photo{width:100%;height:100%;background:radial-gradient(circle at 50% 42%,#c99b7d 0%,#8a6650 45%,#4a3a33 100%)}
.portrait-actions{position:absolute;left:0;top:0;width:100%;height:100%;display:flex;justify-content:center;align-items:center;gap:16px}
.portrait-actions span{width:52px;height:52px;border-radius:50%;background:var(--green);display:flex;align-items:center;justify-content:center}
.member h3{font-weight:400;font-size:22px;color:var(--ink);margin-top:16px}
.member p{font-size:13px;line-height:19px;color:#5a5e56;margin-top:8px;height:76px;overflow:hidden}
.member .btn{margin-top:8px;font-size:18px}

.site-footer{position:absolute;left:0;top:1820px;width:1200px;height:520px;background:linear-gradient(180deg,#6d5a4c 0%,#4a3c33 45%,#2b2420 100%);text-align:center;color:#e8e2da}
.footer-inner{position:absolute;left:250px;top:48px;width:700px}
.footer-inner .rule{width:220px;height:4px;background:rgba(255,255,255,.5);margin:0 auto 18px}
.footer-inner h4{font-weight:300;font-size:28px;letter-spacing:1px}
.footer-inner .tag{font-size:13px;margin-top:8px;opacity:.85}
.footer-inner .phone{font-size:36px;font-weight:300;margin-top:34px}
.footer-inner .addr{font-size:25px;font-weight:300;margin-top:6px}
.footer-inner .mail{font-size:22px;font-weight:300;margin-top:4px}
.to-top{position:absolute;left:588px;top:368px}
.socials{position:absolute;left:0;top:432px;width:1200px;display:flex;justify-content:center;gap:14px}
.socials span{width:34px;height:34px;border-radius:50%;background:var(--green)}
.copyright{position:absolute;left:0;bottom:0;width:1200px;height:30px;background:var(--night);font-size:12px;line-height:30px;color:#cfc7bd}
</style>
</head>
<body>

<div class="hero" role="img" aria-label="Photo of a smiling family of three, mother, father and young son, sitting together on a white sofa"></div>

<header class="site-header">
  <div class="brand"><span class="brand-dot"></span><span class="brand-name">Meadowgate Counselors</span></div>
  <nav class="main-nav">
    <a class="active" href="#">Home</a>
    <a href="#">About</a>
    <a href="#">Contact</a>
  </nav>
</header>

<section class="quote-band">
  <p>“Our sorrows and wounds are healed only when we<br>touch them with compassion.” - Orvelan</p>
</section>

<section class="welcome">
  <h1>Welcome to Meadowgate Counselors</h1>
  <div class="questions">
    Feeling stressed and overwhelmed?<br>
    Encountering barriers towards your goals?<br>
    Having difficulty accomplishing the simplest task?<br>
    Have the need to talk but unsure who to turn to?
  </div>
  <p class="intro">Therapy can assist you in overcoming all of these challenges. Assist you in uncovering the difficulties and barriers that are keeping you from achieving your life’s ambitions, help discover ways to overcome them, and cope with the impact your behaviour has on your occupation, personal life and social life.</p>
  <a class="btn" href="#">Know More</a>
</section>

<section class="about">
  <h2>About Us</h2>
  <div class="team">
    <article class="member">
      <div class="portrait">
        <div class="photo" role="img" aria-label="Portrait of therapist Marisel Dunkworth"></div>
        <div class="portrait-actions">
          <span><svg width="24" height="24" viewBox="0 0 24 24"><path d="M6.6 10.8c1.4 2.8 3.8 5.1 6.6 6.6l2.2-2.2c.3-.3.7-.4 1-.2 1.1.4 2.3.6 3.6.6.6 0 1 .4 1 1V20c0 .6-.4 1-1 1C10.6 21 3 13.4 3 4c0-.6.4-1 1-1h3.5c.6 0 1 .4 1 1 0 1.3.2 2.5.6 3.6.1.3 0 .7-.2 1z" fill="#fff"/></svg></span>
          <span><svg width="26" height="20" viewBox="0 0 26 20"><rect x="1" y="1" width="24" height="18" rx="2" fill="none" stroke="#fff" stroke-width="2"/><path d="M2 3l11 8 11-8" fill="none" stroke="#fff" stroke-width="2"/></svg></span>
        </div>
      </div>
      <h3>Marisel Dunkworth</h3>
      <p>My name is Dr. MariSel Dunkworth and I am a Licensed Marriage Family Therapist with a practice in Riverside, CA.</p>
      <a class="btn" href="#">Know More</a>
    </article>
    <article class="member">
      <div class="portrait"><div class="photo" role="img" aria-label="Portrait of therapist Jeb Kowal"></div></div>
      <h3>Jeb Kowal</h3>
      <p>My name is Rosalindra (Jeb) Kowal, I received my Masters Degree of Counseling in Marriage and Family Therapy from Corvell Bay State College in June 2000.</p>
      <a class="btn" href="#">Know More</a>
    </article>
    <article class="member">
      <div class="portrait"><div class="photo" role="img" aria-label="Portrait of therapist Dena Holcroft"></div></div>
      <h3>Dena Holcroft</h3>
      <p>Dena Holcroft graduated with a Masters in Marriage and Family Therapy from Pellridge Crestwood College.</p>
      <a class="btn" href="#">Know More</a>
    </article>
  </div>
</section>

<footer class="site-footer" role="img" aria-label="Silhouette of a family holding hands against a warm sunset sky">
  <div class="footer-inner">
    <div class="rule"></div>
    <h4>Meadowgate Counselors</h4>
    <p class="tag">Caring support for couples, families and growing children every day.</p>
    <p class="phone">+1 4555 0196</p>
    <p class="addr">20th Street, Area name, City, Country</p>
    <p class="mail">info@meadowgatecounselors.example</p>
  </div>
  <svg class="to-top" width="24" height="20" viewBox="0 0 24 20"><path d="M4 10l8-7 8 7M4 17l8-7 8 7" fill="none" stroke="#fff" stroke-width="2.5"/></svg>
  <div class="socials"><span></span><span></span><span></span></div>
  <div class="copyright">© Meadowgate Counselors. All rights reserved</div>
</footer>

</body>
</html>
```